Web Design Project for Web Agency

WHAT I NEED:
The design I need (PSD file) is for a microsite designed for employee recruitment for Brantley, a Web agency.
***Design for the 1st Page ONLY : "Manifeste"
OBJECTIVES OF THE WEBSITE:
1. To promote the agency's corporate culture and HR management principles.
2. To get people to apply on available jobs
ELEMENTS OF THE PAGE "MANIFESTE" :
1. Brantley logo (see attached files). Beside the logo must be the word "Carrières" ("Careers" in english)
***The logo is not final and there is NO branding for Brantley yet. That is why there are multiple files. So please feel free to be creative!
2. Main menu : 4 sections
Manifeste | Opportunités | Brantly | Postuler
3. Manifeste :
This page is the home page. It will present 2 main sections :
a. The agency's corporate culture :
- Title of the page is a question : "Do you embrace Brantley's corporate culture?"
- Then, presentation of the 5 corporate values, each with a title and short description
- At the end of the list of values, we want a button that says "Apply now"
b. The agency's HR management principles :
- Title of the page is a question : "Do you see yourself working at Brantley?"
- Then, presentation of the 5 Management principles, each with a title and short description
- At the end of the list of principles, we want a button that says "Apply now"
VISUAL INSPIRATION
To create each section of the "Manifeste" page, we want a design that will fit with the corporate culture:
- Brantley is BOLD
- Brantley is PROUD
- Brantley is PROFESSIONAL
- Brantley is ELEGANT
- Brantley is REFINED
We want something slick and modern. Here are some Website's that we like that can be of inspiration:
- http://www.studio-vetrak.com/en/services
- http://quorvinpanels.com/

```html
<!DOCTYPE html>
<html lang="fr">
<head>
<meta charset="utf-8">
<title>Brantley Carrières — Manifeste</title>
<link rel="stylesheet" href="https://fonts.googleapis.com/css2?family=Montserrat:wght@400;600;700&family=Open+Sans:wght@400;600;700&display=swap">
<style>
:root{
  --orange:#f47b3a;
  --grey-heading:#bdbdbd;
  --grey-label:#8a8a8a;
  --text:#333333;
  --rule:#d9d9d9;
  --band:#e6e6e6;
  --white:#ffffff;
}
*{margin:0;padding:0;box-sizing:border-box}
html,body{width:1200px;height:1142px;overflow:hidden;background:var(--white)}
.page{position:relative;width:1200px;height:1142px;font-family:"Open Sans",Arial,sans-serif;color:var(--text)}
.headline{position:absolute;top:104px;left:0;width:1200px;text-align:center;font-family:"Montserrat",Arial,sans-serif;font-weight:600;font-size:29px;line-height:36px;letter-spacing:.32em;color:var(--grey-heading);text-transform:uppercase}
.headline .accent{color:var(--orange);font-weight:700}
.section-label{position:absolute;top:279px;left:0;width:1200px;text-align:center;font-family:"Montserrat",Arial,sans-serif;font-weight:700;font-size:8.5px;letter-spacing:.3em;color:var(--orange)}
.rule{position:absolute;height:1px;background:var(--rule)}
.principle{position:absolute;width:190px}
.principle .photo{position:absolute;width:124px;height:124px;border-radius:50%;border:4px solid var(--orange);overflow:hidden}
.principle .photo div{width:100%;height:100%}
.principle h3{position:absolute;top:142px;left:0;width:160px;text-align:center;font-size:8.5px;font-weight:600;color:var(--grey-label);text-transform:uppercase;letter-spacing:.01em}
.principle p{position:absolute;top:166px;left:0;width:185px;font-size:9.4px;line-height:17px;color:var(--text)}
.apply-button{position:absolute;left:541px;top:854px;width:120px;height:31px;background:var(--orange);color:var(--white);font-family:"Montserrat",Arial,sans-serif;font-weight:700;font-size:8.5px;letter-spacing:.3em;text-align:center;line-height:31px;text-transform:uppercase}
.footer-band{position:absolute;top:945px;left:0;width:1200px;height:96px;background:var(--band)}
.main-nav{position:absolute;left:349px;top:985px;display:flex;font-size:8.5px;font-weight:700;color:var(--orange);text-transform:uppercase}
.main-nav span{padding:0 7px;border-left:1px solid #cfcfcf;line-height:11px}
.main-nav span:first-child{padding-left:0;border-left:0}
.brand{position:absolute;left:624px;top:975px;height:40px;border-left:1px solid #cfcfcf;padding-left:18px}
.brand-name{font-family:"Open Sans",Arial,sans-serif;font-weight:600;font-size:25px;color:#8c8c8c;line-height:30px}
.brand-tagline{font-size:5.5px;letter-spacing:.45em;color:#9a9a9a;margin-top:1px;padding-left:6px}
.brand-careers{position:absolute;left:772px;top:983px;border-left:1px solid #cfcfcf;padding-left:7px;font-weight:700;font-size:15px;color:#b5b5b5;line-height:20px}
.contact{position:absolute;top:1052px;left:0;width:1200px;text-align:center;font-size:7.5px;letter-spacing:.3em;line-height:11px;color:var(--grey-label);text-transform:uppercase}
.contact .accent,.copyright .accent{color:var(--orange)}
.copyright{position:absolute;top:1099px;left:0;width:1200px;text-align:center;font-size:7.5px;letter-spacing:.3em;color:var(--grey-label);text-transform:uppercase}
</style>
</head>
<body>
<div class="page">
  <h1 class="headline">Do you see yourself<br>working at <span class="accent">Brantley</span>?</h1>

  <div class="rule" style="left:302px;top:282px;width:162px"></div>
  <div class="section-label">5 Management principles</div>
  <div class="rule" style="left:743px;top:282px;width:162px"></div>

  <div class="principle" style="left:301px;top:340px">
    <div class="photo" style="left:19px;top:0"><div role="img" aria-label="Black and white photo of a hand holding a paper plane" style="background:radial-gradient(circle at 40% 40%,#e8e8e8,#8c8c8c)"></div></div>
    <h3>Set high objectives</h3>
    <p>Lorem ipsum dolor sit amet, consectetur adipiscing elit. Sed pellentesque, purus sit amet pulvinar sollicitudin, nulla odio hen-</p>
  </div>
  <div class="principle" style="left:506px;top:340px">
    <div class="photo" style="left:30px;top:0"><div role="img" aria-label="Black and white photo of darts on a dartboard" style="background:radial-gradient(circle at 50% 45%,#9a9a9a,#2e2e2e)"></div></div>
    <h3 style="left:10px">Set specific goals</h3>
    <p>Lorem ipsum dolor sit amet, consectetur adipiscing elit. Sed pellentesque, purus sit amet pulvinar sollicitudin, nulla odio hen-</p>
  </div>
  <div class="principle" style="left:721px;top:340px">
    <div class="photo" style="left:24px;top:0"><div role="img" aria-label="Black and white photo of a painter's hand and brush" style="background:radial-gradient(circle at 45% 45%,#c4c4c4,#6a6a6a)"></div></div>
    <h3 style="left:6px">Keep a passionate</h3>
    <p>Lorem ipsum dolor sit amet, consectetur adipiscing elit. Sed pellentesque, purus sit amet pulvinar sollicitudin, nulla odio hen-</p>
  </div>

  <div class="principle" style="left:406px;top:590px">
    <div class="photo" style="left:32px;top:0"><div role="img" aria-label="Black and white photo of interlocking metal gears" style="background:radial-gradient(circle at 50% 50%,#a0a0a0,#3a3a3a)"></div></div>
    <h3 style="left:13px">Solid team player</h3>
    <p>Lorem ipsum dolor sit amet, consectetur adipiscing elit. Sed pellentesque, purus sit amet pulvinar sollicitudin, nulla odio hen-</p>
  </div>
  <div class="principle" style="left:621px;top:590px">
    <div class="photo" style="left:26px;top:0"><div role="img" aria-label="Close-up photo of a human eye" style="background:radial-gradient(circle at 50% 50%,#b07a40,#cfcfcf 30%,#8f8f8f)"></div></div>
    <h3 style="left:0">Face every challenge</h3>
    <p>Lorem ipsum dolor sit amet, consectetur adipiscing elit. Sed pellentesque, purus sit amet pulvinar sollicitudin, nulla odio hen-</p>
  </div>

  <div class="rule" style="left:302px;top:869px;width:196px"></div>
  <div class="apply-button">Apply now</div>
  <div class="rule" style="left:704px;top:869px;width:196px"></div>

  <div class="footer-band"></div>
  <nav class="main-nav"><span>Manifeste</span><span>Opportunités</span><span>Brantly</span><span>Postuler</span></nav>
  <div class="brand">
    <div class="brand-name">Brantley</div>
    <div class="brand-tagline">AGENCE NUMÉRIQUE</div>
  </div>
  <div class="brand-careers">Carrières</div>

  <div class="contact">Brantley, 48 Orrin Street suite 13th, lorem ipsum dolor sit amet, 9210, mortem<br>T: <span class="accent">1800-462915</span> . F: <span class="accent">700-518372</span> . E: <span class="accent">enquiry@brantley.com</span></div>
  <div class="copyright">Copyright ©2013 <span class="accent">Brantley Carrières</span></div>
</div>
</body>
</html>
```